Flyer für Tiertherapeutin
Eine sehr motivierte und kreative Designerin. Schon der erste Vorschlag war ganz nach meinen Vorstellungen.
Zielgruppe
Ich bin Tiertherapeutin für TCVM und Ernährungsberaterin für Hunde und Katzen. Mittels Akupunktur, Lasertherapie, Mykotherapie und Ernährungsberatung kommt es zu einer Linderung vorhandener Schmerzen, eine verbesserte Regulation der Organe und einer Steigerung das Wohlbefindens sowie Lebensqualität.
Zielgruppe sind überwiegend weibliche Hunde- und Katzenbesitzer mit erkrankten Tieren.
Aufgabenstellung
Flyer sollte klappbar sein. Logo und mein Name und Kontaktdaten sollten enthalten sein.

```html
<!DOCTYPE html>
<html lang="de">
<head>
<meta charset="utf-8">
<title>Pfotenmitte – Flyer</title>
<link href="https://fonts.googleapis.com/css2?family=Open+Sans:wght@400;600;700&family=Dancing+Script:wght@600&display=swap" rel="stylesheet">
<style>
  :root{
    --tan:#d29a68;
    --tan-text:#c98f5c;
    --orange:#e08b2c;
    --orange-deep:#d97c1c;
    --orange-line:#c9741c;
    --cream:#fbe3c4;
    --brown-dark:#4a3f30;
    --ink:#1f1f1f;
    --white:#ffffff;
  }
  *{margin:0;padding:0;box-sizing:border-box}
  html,body{width:1200px;height:635px;overflow:hidden;background:var(--white)}
  .flyer{position:relative;width:1200px;height:635px;overflow:hidden;font-family:'Open Sans',sans-serif;color:var(--ink)}
  .backdrop{position:absolute;inset:0}
  .abs{position:absolute}
  .column{width:247px}
  .script-heading{font-family:'Dancing Script',cursive;font-weight:600;color:var(--tan-text);font-size:25px;line-height:1}
  .body-text{font-size:8.4px;letter-spacing:-0.1px;line-height:14.9px}
  .body-text .ln{display:block;white-space:nowrap;text-align:justify;text-align-last:justify}
  .body-text .ln.end{text-align-last:left}
  .sub-heading{font-size:8.4px;font-weight:700;line-height:14.9px}
  .benefits{list-style:none}
  .benefits li{position:relative;padding-left:27px;font-size:8.4px;line-height:11.8px;white-space:nowrap;margin-bottom:4px}
  .benefits li::before{content:"";position:absolute;left:8px;top:4px;width:3.5px;height:3.5px;border-radius:50%;background:var(--ink)}
  .photo-circle{position:absolute;width:184px;height:184px;border-radius:50%;border:4.5px solid var(--white)}
  .photo-cells{left:51px;top:416px;background:radial-gradient(circle at 40% 35%,#fff3e6 0%,#f3d2b2 45%,#e7b07c 80%,#d9964f 100%)}
  .photo-food{left:333px;top:416px;background:radial-gradient(circle at 50% 55%,#c9664a 0%,#8e3a2c 35%,#d77a3a 65%,#1a1a1a 100%)}
  .cta{position:absolute;left:592px;width:303px;text-align:center;color:var(--cream)}
  .cta-heart{position:absolute;left:731px;top:72px}
  .cta-small{font-size:8.3px;line-height:15px}
  .cta-script{font-family:'Dancing Script',cursive;font-weight:600;color:var(--white);font-size:27px;line-height:1}
  .cta-label{font-size:8.6px;font-weight:700;color:var(--white);line-height:15px}
  .contact{position:absolute;left:657px;top:499px;color:var(--cream);font-size:8.6px;line-height:14.8px;font-style:normal}
  .contact strong{color:var(--white);font-weight:700}
  .contact .gap{height:14.8px}
  .brand{position:absolute;left:895px;width:305px;text-align:center;color:var(--ink);font-weight:700}
  .brand-name{top:150px;font-size:27px;line-height:1}
  .brand-owner{top:201px;font-size:11px;letter-spacing:3.6px}
  .services{position:absolute;left:895px;width:305px;top:518px;text-align:center;color:var(--white)}
  .services .line{font-size:18.5px;line-height:22px}
  .services .region{font-size:12.3px;margin-top:3px}
</style>
</head>
<body>
<div class="flyer">
  <svg class="backdrop" width="1200" height="635" viewBox="0 0 1200 635">
    <defs>
      <linearGradient id="petPhotoTone" x1="0" y1="0" x2="0" y2="1">
        <stop offset="0" stop-color="#ffffff"/>
        <stop offset="0.3" stop-color="#f3f1ea"/>
        <stop offset="0.5" stop-color="#d8d2b6"/>
        <stop offset="0.7" stop-color="#c98a4a"/>
        <stop offset="1" stop-color="#a87a55"/>
      </linearGradient>
    </defs>
    <g role="img" aria-label="Foto: Katze und Hund liegen nebeneinander im Freien">
      <path d="M895 0 H1200 V507 Q1050 490 895 481 Z" fill="url(#petPhotoTone)"/>
    </g>
    <rect x="592" y="0" width="303" height="635" fill="var(--orange)"/>
    <path d="M592 494 Q743 488 895 494 V635 H592 Z" fill="var(--orange-deep)"/>
    <path d="M592 481 Q743 476 895 481" fill="none" stroke="var(--orange-line)" stroke-width="1.5"/>
    <path d="M0 533 Q300 500 592 481" fill="none" stroke="var(--brown-dark)" stroke-width="6"/>
    <path d="M0 552 Q300 512 592 494 V635 H0 Z" fill="var(--tan)"/>
    <path d="M895 481 Q1050 490 1200 507" fill="none" stroke="var(--brown-dark)" stroke-width="6"/>
    <path d="M895 494 Q1050 500 1200 515 V635 H895 Z" fill="var(--tan)"/>
  </svg>

  <!-- Panel: Lasertherapie -->
  <h2 class="abs script-heading" style="left:28px;top:42px">Lasertherapie</h2>
  <p class="abs column body-text" style="left:28px;top:78px">
    <span class="ln">Die Lasertherapie beruht auf physikalische Ereignisse. Die La-</span>
    <span class="ln">sertherapie wirkt von der atomaren Ebene bis zur mikrosko-</span>
    <span class="ln">pischen Ebene der Gewebe. Durch das gebündelte Laserlicht</span>
    <span class="ln">wird Energie in die Zellen unseres Körpers transportiert. Die</span>
    <span class="ln">Kraftantreiber (Mitochondrien) unserer Zellen nehmen diese</span>
    <span class="ln end">Energie auf und bauen sie direkt in Zellenergie um (ATP).</span>
  </p>
  <p class="abs column body-text" style="left:28px;top:180px">
    <span class="ln">Die Beeinflussung der Zellenergie fördert alle Lebensvorgänge.</span>
    <span class="ln">Durch die hinzugefügte Energie des Lasers in den Zellen, ist es</span>
    <span class="ln">dem Körper erst möglich wichtige Stoffwechselprozesse voran-</span>
    <span class="ln end">zutreiben.</span>
  </p>
  <h3 class="abs sub-heading" style="left:28px;top:253px">Welche Wirkung hat die Lasertherapie?</h3>
  <ul class="abs benefits" style="left:28px;top:279px">
    <li>Förderung der Wundheilung, entzündungshemmend<br>durch Anregung des zellulären Stoffwechsels</li>
    <li>Durchblutungsfördernd, antibakteriell</li>
    <li>Anzahl spezifischer Enzyme steigen</li>
    <li>Förderung der Kapillarisation</li>
    <li>Narbenentstörung</li>
    <li>Vermehrung von Kollagenfasern</li>
    <li>Erhöhung der Antikörperbildung</li>
    <li>Verstärkung der Gefäßneubildung</li>
  </ul>
  <div class="photo-circle photo-cells" role="img" aria-label="Foto: Nahaufnahme von Zellstrukturen mit goldenen Tropfen"></div>

  <!-- Panel: Ernährungsberatung -->
  <h2 class="abs script-heading" style="left:318px;top:42px">Ernährungsberatung</h2>
  <p class="abs column body-text" style="left:318px;top:78px">
    <span class="ln">Ich als Tierernährungsberaterin habe mich auf die Ernährung</span>
    <span class="ln">von Hunden und Katzen spezialisiert und biete dir eine um-</span>
    <span class="ln">fassende Beratung und Unterstützung in Bezug auf die Ernäh-</span>
    <span class="ln">rungsbedürfnisse deines Tieres. Der Markt an Futtermitteln ist</span>
    <span class="ln">im Laufe der Zeit riesig geworden. Es ist für den Laien teilweise</span>
    <span class="ln">schwierig geworden, zu überprüfen, ob mein Tier wirklich die-</span>
    <span class="ln">ses Futtermittel benötigt oder ob es sich nur um ein Werbever-</span>
    <span class="ln end">sprechen handelt.</span>
  </p>
  <h3 class="abs sub-heading" style="left:318px;top:210px">Ich berate dich gern zu folgenden Themen:</h3>
  <ul class="abs benefits" style="left:318px;top:237px">
    <li>Welches Futtermittel ist für mein Tier und den<br>damit verbundenen Bedürfnissen das richtige?</li>
    <li>Entwicklung von Ernährungsplänen: Basierend auf den<br>spezifischen Bedürfnissen deines Tieres</li>
    <li>Gesundheitsmanagement: Adipositas (Fettleibigkeit)<br>oder Kachexie (pathologischer Gewichtsverlust)</li>
    <li>Beratung bei Erkrankungen: Durch gezielte Futter-<br>umstellung die Symptomatik deines Tieres verbessern</li>
    <li>Darmfloraaufbau: Gezielter Darmfloraaufbau lindert<br>Durchfall, hilft deinem Tier ein gesundes Gewicht<br>erreichen, verbessert die Fellqualität und senkt die<br>Infektanfälligkeit</li>
  </ul>
  <div class="photo-circle photo-food" role="img" aria-label="Foto: Rohes Fleisch, Innereien, Gemüse und Karotten für Tierfutter"></div>

  <!-- Panel: Erstberatung -->
  <svg class="cta-heart" width="24" height="21" viewBox="0 0 24 21" aria-hidden="true">
    <path d="M12 20 C4 14 0 10 0 5.5 C0 2.4 2.4 0 5.4 0 C8 0 10.5 1.6 12 3.8 C13.5 1.6 16 0 18.6 0 C21.6 0 24 2.4 24 5.5 C24 10 20 14 12 20 Z" fill="var(--white)"/>
  </svg>
  <div class="cta" style="top:94px">
    <p class="cta-small">Neugierig? Jetzt Termin für die</p>
    <p class="cta-script" style="margin-top:2px">kostenlose Erstberatung</p>
    <p class="cta-small">vereinbaren.</p>
  </div>
  <div class="cta" style="top:173px">
    <p class="cta-label">Online</p>
    <p class="cta-small">entspannt von zuhause</p>
    <p class="cta-small">per Videokonferenz</p>
    <p class="cta-label" style="margin-top:8px">Hausbesuche</p>
    <p class="cta-small">im Raum Karlsruhe auch vor</p>
    <p class="cta-small">Ort für dich im Einsatz</p>
  </div>
  <address class="contact">
    <strong>Marlene Brandt</strong><br>
    Ahornweg 12<br>
    76135 Karlsruhe
    <div class="gap"></div>
    0176 - 4810 2937<br>
    info@pfotenmitte.de<br>
    www.pfotenmitte.de
  </address>

  <!-- Panel: Titel -->
  <p class="brand brand-name">Pfotenmitte</p>
  <p class="brand brand-owner">MARLENE BRANDT</p>
  <div class="services">
    <p class="line">Tierernährungsberatung</p>
    <p class="line">TCVM • Akupunktur</p>
    <p class="region">in Karlsruhe und Umgebung</p>
  </div>
</div>
</body>
</html>
```